Redesign Colorful Business Card

Please redesign the card attached. It is too busy. Please don't eliminate any of the words. The repetivite word "free" can be used less often.

Target Market(s)

College Students.

Contact Information for Business Card

The details listed in the attached image

Font styles to use
Sans Serif

Requirements
Must have
• A clear and simple presentation and must be attractive.

```html
<!DOCTYPE html>
<html lang="en">
<head>
<meta charset="utf-8">
<title>Study Brisk – Card</title>
<link rel="stylesheet" href="https://fonts.googleapis.com/css2?family=Poppins:wght@500;600;800&family=Montserrat:wght@500;600&display=swap">
<style>
  :root{
    --band:#654af5;
    --sky-pink:#f24fcf;
    --soft-pink:#f6a8dc;
    --peach:#f7c9b4;
    --sun:#efe300;
    --pill-violet:#5846f0;
    --pill-violet-2:#6c5cf2;
    --pill-pink:#ee4fe0;
    --pill-pink-2:#f25ae6;
    --pill-orange:#f0563f;
    --pill-orange-2:#f7621c;
    --free-blue:#0a22d6;
    --url-purple:#6b1aa8;
    --mascot-a:#8a5cf0;
    --mascot-b:#e548d8;
    --white:#ffffff;
  }
  *{box-sizing:border-box;margin:0;padding:0}
  html,body{width:1200px;height:758px;overflow:hidden;background:var(--white)}
  .canvas{position:relative;width:1200px;height:758px;background:var(--white);font-family:"Poppins",sans-serif}
  .card{position:absolute;left:86px;top:86px;width:1028px;height:587px;overflow:hidden;background:var(--white)}
  .band-top{position:absolute;left:0;top:0;width:100%;height:22px;background:var(--band)}
  .wash{position:absolute;left:0;top:22px;width:100%;height:479px;
    background:linear-gradient(180deg,var(--sky-pink) 0%,#f479d4 25%,var(--soft-pink) 45%,var(--peach) 68%,#f3e07a 85%,var(--sun) 100%)}
  .frame{position:absolute;left:0;top:0;width:1028px;height:587px}
  .mascot{position:absolute;left:610px;top:150px;width:345px;height:322px;border-radius:110px 140px 26px 26px;
    border:4px solid var(--white);
    background:linear-gradient(135deg,var(--mascot-a),var(--mascot-b))}
  .free{position:absolute;left:540px;top:56px;z-index:2;font-weight:800;font-size:66px;line-height:1;letter-spacing:-1px;
    color:var(--free-blue);-webkit-text-stroke:5px var(--white);paint-order:stroke fill}
  .benefit{position:absolute;left:181px;width:346px;height:89px;border-radius:0 45px 45px 0;
    color:var(--white);font-weight:500;font-size:24px;line-height:30px;padding:15px 0 0 28px;
    box-shadow:0 4px 10px rgba(0,0,0,.12)}
  .benefit--time{top:142px;background:linear-gradient(90deg,var(--pill-violet),var(--pill-violet-2))}
  .benefit--remote{top:249px;background:linear-gradient(90deg,var(--pill-pink-2),var(--pill-pink))}
  .benefit--memory{top:356px;background:linear-gradient(90deg,var(--pill-orange),var(--pill-orange-2))}
  .icon{position:absolute;left:82px;width:80px;height:80px}
  .icon--time{top:146px}
  .icon--remote{top:252px}
  .icon--memory{top:360px}
  .web{position:absolute;left:0;top:501px;width:100%;height:47px;background:var(--white);
    display:flex;align-items:center;justify-content:center;
    font-family:"Montserrat",sans-serif;font-weight:600;font-size:29px;letter-spacing:.52em;color:var(--url-purple);padding-left:.52em}
  .band-bottom{position:absolute;left:0;top:548px;width:100%;height:39px;background:var(--band);
    display:flex;align-items:center;justify-content:center;
    font-family:"Montserrat",sans-serif;font-weight:500;font-size:15px;letter-spacing:1.4px;color:var(--white)}
</style>
</head>
<body>
<div class="canvas">
  <div class="card">
    <div class="band-top"></div>
    <div class="wash"></div>

    <svg class="frame" viewBox="0 0 1028 587" aria-hidden="true">
      <path d="M61 100 H525 V50 H764 V133 H552 V481 H61 Z" fill="none" stroke="#fff" stroke-width="2.5" stroke-dasharray="9 6"/>
      <polygon points="40,110 80,92 100,102 60,122" fill="#fff"/>
      <path d="M56 118 V132 Q70 140 84 130 V112" fill="#fff"/>
      <path d="M50 114 Q48 130 44 144" stroke="#fff" stroke-width="2" fill="none"/>
    </svg>

    <div class="mascot" role="img" aria-label="Illustration of a colourful elephant with raised trunk"></div>

    <div class="free">FREE!!</div>

    <svg class="icon icon--time" viewBox="0 0 80 80" aria-hidden="true">
      <circle cx="36" cy="36" r="32" fill="#fff"/>
      <circle cx="36" cy="36" r="27" fill="#5d49f0"/>
      <circle cx="36" cy="36" r="21" fill="#fff"/>
      <path d="M36 22 V37 H47" stroke="#5d49f0" stroke-width="4" fill="none" stroke-linecap="round"/>
      <circle cx="60" cy="60" r="17" fill="#fff"/>
      <circle cx="60" cy="60" r="13" fill="#5d49f0"/>
      <path d="M60 52 V66 M54 61 L60 67 L66 61" stroke="#fff" stroke-width="3" fill="none" stroke-linecap="round"/>
    </svg>

    <svg class="icon icon--remote" viewBox="0 0 80 80" aria-hidden="true">
      <path d="M6 40 L38 12 L70 40 V76 H6 Z" fill="#fff"/>
      <path d="M14 42 L38 21 L62 42 V70 H14 Z" fill="#ee4fe0"/>
      <rect x="26" y="46" width="24" height="24" rx="4" fill="#fff"/>
      <circle cx="60" cy="18" r="16" fill="#fff"/>
      <circle cx="60" cy="18" r="12" fill="#ee4fe0"/>
      <path d="M54 18 L58 22 L66 13" stroke="#fff" stroke-width="3" fill="none" stroke-linecap="round"/>
    </svg>

    <svg class="icon icon--memory" viewBox="0 0 80 80" role="img" aria-label="Icon of a bright idea">
      <g stroke="#fff" stroke-width="3" stroke-linecap="round">
        <path d="M40 4 V12 M18 10 L23 17 M62 10 L57 17 M4 26 H12 M68 26 H76"/>
      </g>
      <rect x="18" y="22" width="44" height="54" rx="18" fill="#fff"/>
      <rect x="23" y="27" width="34" height="44" rx="14" fill="#f0563f"/>
    </svg>

    <div class="benefit benefit--time">Cut study time down<br>by upto 50%</div>
    <div class="benefit benefit--remote">Learn a subject without<br>having to go to class</div>
    <div class="benefit benefit--memory">Memorize anything<br>quickly.</div>

    <div class="web">WWW.STUDYBRISK.COM</div>
    <div class="band-bottom">copyright brisk study services,llc 2013-2022 all rights reserved</div>
  </div>
</div>
</body>
</html>
```